Pop Up Banner Design (30x72in) for events for Tavoren Study House

30 x 72 inch design for a pop up banner or 2 (or 3) to advertise my business, Tavoren Study House, featuring www.tavorenstudyhouse.com

This banner will be used at anime conventions, or local events to promote the business to the general public, schools, or asian culture lovers.

Color scheme to identify with the logo that is attached. Imagery would be great!

Target audience: teens to 30s
Benefits TSH Offers: learning japanese language, learning japanese culture, peer study groups and events, one-on-one or classroom setting, in person or virtual learning, Brenwick Tongue Mastery Exam (BTME) preparation, homework, guided tours to Japan once a year, translation services, conversation tables, etc.

Target Market(s)

teens to 30 year olds

Industry/Entity Type

Education

Font styles to use
Sans Serif

Colors
ec1f27
ffffff
000000

Requirements
Must have
• logo, imagery, benefits strategically explained, website

```html
<!DOCTYPE html>
<html lang="en">
<head>
<meta charset="utf-8">
<title>Tavoren Study House – Event Banner</title>
<link rel="stylesheet" href="https://fonts.googleapis.com/css2?family=Roboto+Condensed:wght@400;700&family=Lato:wght@300;400&family=Arimo:wght@700&display=swap">
<style>
  :root {
    --brand-red: #c1272d;
    --white: #ffffff;
    --ink: #111111;
    --photo-green-light: #7fb35a;
    --photo-green-dark: #2f5a24;
    --photo-sky: #a9c98a;
  }
  * { margin: 0; padding: 0; box-sizing: border-box; }
  html, body { width: 1200px; height: 500px; overflow: hidden; background: var(--white); }
  .banner {
    position: relative;
    width: 1200px;
    height: 500px;
    background: var(--white);
    overflow: hidden;
  }
  .brand-panel {
    position: absolute;
    left: 0; top: 0;
    width: 600px; height: 500px;
    background: var(--white);
  }
  .hero-photo {
    position: absolute;
    left: 0; top: 0;
    width: 600px; height: 350px;
    background:
      radial-gradient(ellipse at 50% 30%, var(--photo-sky) 0%, transparent 55%),
      linear-gradient(180deg, var(--photo-green-dark) 0%, #4d7f34 45%, var(--photo-green-light) 70%, #6fa84a 100%);
  }
  .brand-mark {
    position: absolute;
    left: 222px; top: 222px;
    width: 180px; height: 180px;
    border-radius: 50%;
    background: var(--brand-red);
    border: 6px solid var(--white);
  }
  .brand-name {
    position: absolute;
    left: 0; top: 400px;
    width: 600px;
    text-align: center;
    font-family: "Lato", sans-serif;
    font-weight: 400;
    font-size: 30px;
    line-height: 40px;
    letter-spacing: 0.5px;
    text-transform: uppercase;
    color: var(--ink);
  }
  .brand-url {
    position: absolute;
    left: 0; top: 454px;
    width: 600px;
    text-align: center;
    font-family: "Arimo", sans-serif;
    font-weight: 700;
    font-size: 17px;
    line-height: 24px;
    color: var(--ink);
  }
  .benefits-panel {
    position: absolute;
    left: 600px; top: 0;
    width: 600px; height: 500px;
    background: var(--brand-red);
    color: var(--white);
    font-family: "Roboto Condensed", sans-serif;
    font-size: 24px;
    line-height: 35px;
    padding: 57px 0 0 29px;
  }
  .benefits-heading {
    font-size: 24px;
    line-height: 35px;
    font-weight: 700;
    white-space: nowrap;
  }
  .benefit-list { list-style: none; }
  .benefit-list li { white-space: nowrap; }
  .benefit-list li::before { content: "\2022\00a0"; }
  .benefit-list .plain::before { content: ""; }
  .exam-block { margin-top: 35px; }
</style>
</head>
<body>
<main class="banner">
  <section class="brand-panel">
    <div class="hero-photo" role="img" aria-label="Group of smiling young students holding notebooks in a green park"></div>
    <div class="brand-mark" aria-hidden="true"></div>
    <h1 class="brand-name">Tavoren Study House</h1>
    <p class="brand-url">www.tavorenstudyhouse.com</p>
  </section>

  <section class="benefits-panel">
    <h2 class="benefits-heading">Benefits TSH Offers:</h2>
    <ul class="benefit-list">
      <li class="plain">Learning Japanese Language</li>
      <li>Learning Japanese Culture</li>
      <li>Peer Study Groups And Events</li>
      <li>One-on-one Or Classroom Setting</li>
      <li>In Person Or Virtual Learning</li>
    </ul>

    <div class="exam-block">
      <h2 class="benefits-heading">Brenwick Tongue Mastery Exam (BTME)</h2>
      <ul class="benefit-list">
        <li>Preparation &bull; Homework</li>
        <li>Guided tours to Japan once a year</li>
        <li>Translation Services &bull; Conversation Tables, etc.</li>
      </ul>
    </div>
  </section>
</main>
</body>
</html>
```